Heronby Mortgage Capital Business Card

We need a business card design for our mortgage servicing company. In addition to servicing the loans of homeowners, we help homeowners with purchasing their homes and any mortgage refinancing. We would like to see designs that use the colors in the logo attached below (gold-ish yellow and navy blue), and any other design you deem fit! The design should communicate a simpler life with smart mortgages provided by Heronby.

```html
<!DOCTYPE html>
<html lang="en">
<head>
<meta charset="utf-8">
<title>Heronby Mortgage Capital – Business Card</title>
<link rel="stylesheet" href="https://fonts.googleapis.com/css2?family=Oswald:wght@400;500&family=Rubik:wght@400&display=swap">
<style>
  :root {
    --gold: #d4a72c;
    --gold-light: #e3bf58;
    --gold-dark: #bb8f1c;
    --navy: #23204f;
    --card-white: #f7f7f8;
    --rule: #b9b8c6;
    --backdrop: #e6e4df;
  }
  * { box-sizing: border-box; margin: 0; padding: 0; }
  html, body { width: 1200px; height: 900px; overflow: hidden; }
  body {
    background: var(--backdrop);
    display: flex;
    flex-direction: column;
    align-items: center;
    justify-content: center;
    gap: 36px;
    font-family: "Rubik", Arial, sans-serif;
  }
  .card {
    position: relative;
    width: 700px;
    height: 400px;
    overflow: hidden;
    box-shadow: 0 6px 18px rgba(0,0,0,0.15);
  }

  /* Front side */
  .card-front { background: var(--card-white); }
  .front-logo {
    position: absolute;
    left: 60px;
    top: 62px;
    font-family: "Oswald", Arial, sans-serif;
    font-weight: 500;
    font-size: 34px;
    color: var(--navy);
    letter-spacing: 0.5px;
  }
  .divider {
    position: absolute;
    height: 1px;
    background: var(--rule);
  }
  .divider-main { left: 60px; top: 170px; width: 385px; }
  .divider-name { left: 600px; top: 92px; width: 60px; }
  .identity {
    position: absolute;
    right: 110px;
    top: 68px;
    text-align: left;
  }
  .person-name {
    font-family: "Oswald", Arial, sans-serif;
    font-weight: 500;
    font-size: 38px;
    line-height: 1;
    color: var(--navy);
  }
  .person-title {
    font-family: "Oswald", Arial, sans-serif;
    font-weight: 400;
    font-size: 17px;
    color: var(--gold);
    margin-top: 8px;
    letter-spacing: 0.3px;
  }
  .contact-list {
    position: absolute;
    left: 60px;
    top: 198px;
    list-style: none;
  }
  .contact-item {
    display: flex;
    align-items: center;
    gap: 18px;
    height: 30px;
    font-size: 16px;
    color: var(--navy);
  }
  .contact-icon { width: 18px; height: 18px; flex: none; }
  .band-gold {
    position: absolute;
    left: 0; bottom: 0;
    width: 560px; height: 28px;
    background: var(--gold);
  }
  .band-navy {
    position: absolute;
    right: 0; bottom: 0;
    width: 140px; height: 44px;
    background: var(--navy);
  }

  /* Back side */
  .card-back {
    background: linear-gradient(135deg, var(--gold-light) 0%, var(--gold) 45%, var(--gold-dark) 100%);
    display: flex;
    align-items: center;
    justify-content: center;
  }
  .back-logo {
    font-family: "Oswald", Arial, sans-serif;
    font-weight: 500;
    font-size: 64px;
    color: var(--navy);
    letter-spacing: 1px;
  }
</style>
</head>
<body>
  <section class="card card-front" aria-label="Business card front">
    <div class="front-logo">Heronby Mortgage</div>
    <div class="divider divider-main"></div>
    <div class="divider divider-name"></div>
    <div class="identity">
      <div class="person-name">Daniel Reyes</div>
      <div class="person-title">Managing Director</div>
    </div>
    <ul class="contact-list">
      <li class="contact-item">
        <svg class="contact-icon" viewBox="0 0 24 24" fill="none" stroke="#d4a72c" stroke-width="1.8" stroke-linejoin="round">
          <path d="M5 3h4l2 5-2.5 1.5a11 11 0 0 0 6 6L16 13l5 2v4a2 2 0 0 1-2 2A16 16 0 0 1 3 5a2 2 0 0 1 2-2z"/>
        </svg>
        <span>+1 555 014 2290</span>
      </li>
      <li class="contact-item">
        <svg class="contact-icon" viewBox="0 0 24 24" fill="none" stroke="#d4a72c" stroke-width="1.8" stroke-linejoin="round">
          <rect x="3" y="5" width="18" height="14" rx="1"/>
          <path d="M3 6l9 7 9-7"/>
        </svg>
        <span>info@heronbymortgage.com</span>
      </li>
      <li class="contact-item">
        <svg class="contact-icon" viewBox="0 0 24 24" fill="none" stroke="#d4a72c" stroke-width="1.8">
          <circle cx="12" cy="12" r="9"/>
          <ellipse cx="12" cy="12" rx="4" ry="9"/>
          <path d="M3 12h18M5 7h14M5 17h14"/>
        </svg>
        <span>www.heronbymortgage.com</span>
      </li>
      <li class="contact-item">
        <svg class="contact-icon" viewBox="0 0 24 24" fill="none" stroke="#d4a72c" stroke-width="1.8" stroke-linejoin="round">
          <path d="M12 22s7-7 7-12a7 7 0 0 0-14 0c0 5 7 12 7 12z"/>
          <circle cx="12" cy="10" r="2.5"/>
        </svg>
        <span>418 Alder Creek Lane, Portland</span>
      </li>
    </ul>
    <div class="band-gold"></div>
    <div class="band-navy"></div>
  </section>

  <section class="card card-back" aria-label="Business card back">
    <div class="back-logo">Heronby Mortgage</div>
  </section>
</body>
</html>
```